Marta Quinlan Photography needs a unique, creative business card/logo design

I need a design for business cards/logo that is unique and creative in the industry. Simplicity is nice, so not too crowded. Something that will catch my customer's eye and remain in their memory. I am primarily a landscape photographer but will be soon may be branching into boudoir photography as well. I have attached my current card.

Industry/Entity Type

Business

Contact Information for Business Card

Marta Quinlan Photography
Phone: 0439 271 504
Email: MartaQuinlanPhotography@brivomail.net
Website: www.pagerly.net/MartaQuinlanPhotography.Aust

Logo Text

Marta Quinlan Photography

Requirements
Must have
• Contact Details on one side
Should not have
• pixelation

```html
<!DOCTYPE html>
<html lang="en">
<head>
<meta charset="utf-8">
<title>Marta Quinlan Photography – Business Card</title>
<link href="https://fonts.googleapis.com/css2?family=Playfair+Display:wght@400&display=swap" rel="stylesheet">
<style>
  :root {
    --backdrop: #2b2b2c;
    --paper: #f4f4f4;
    --paper-shade: #e2e2e3;
    --teal: #1db3a3;
    --teal-deep: #13968a;
    --teal-ink: #2bbfb0;
    --ink: #3a3a3c;
    --soft-white: #eef1f0;
  }
  * { margin: 0; padding: 0; box-sizing: border-box; }
  html, body {
    width: 1200px;
    height: 873px;
    overflow: hidden;
    background: var(--backdrop);
  }
  .stage {
    position: relative;
    width: 1200px;
    height: 873px;
    font-family: "Playfair Display", Georgia, serif;
  }
  .card {
    position: absolute;
    width: 540px;
    height: 310px;
    border-radius: 16px;
    overflow: hidden;
  }
  .card-back {
    left: 70px;
    top: 110px;
    background: linear-gradient(135deg, var(--paper) 0%, var(--paper-shade) 100%);
  }
  .card-front {
    left: 590px;
    top: 440px;
    background: linear-gradient(135deg, var(--teal) 0%, var(--teal-deep) 100%);
  }
  .texture {
    position: absolute;
    inset: 0;
  }
  .card-back .texture {
    background: radial-gradient(circle at 40% 30%, rgba(255,255,255,0.7), rgba(255,255,255,0) 70%);
  }
  .card-front .texture {
    background: radial-gradient(circle at 30% 25%, rgba(255,255,255,0.12), rgba(255,255,255,0) 65%);
  }
  .wordmark {
    position: absolute;
    left: 0;
    right: 0;
    text-align: center;
    font-weight: 400;
  }
  .wordmark .mark-dot {
    display: block;
    margin: 0 auto 14px;
    border-radius: 50%;
  }
  .wordmark .name { display: block; line-height: 1.05; }
  .wordmark .trade {
    display: block;
    letter-spacing: 0.55em;
    text-transform: uppercase;
    margin-top: 6px;
    padding-left: 0.55em;
  }
  .card-back .wordmark { top: 46px; color: var(--teal-ink); }
  .card-back .mark-dot { width: 70px; height: 70px; background: var(--teal-ink); }
  .card-back .name { font-size: 30px; }
  .card-back .trade { font-size: 11px; }

  .card-front .wordmark { top: 52px; color: var(--soft-white); }
  .card-front .mark-dot { width: 96px; height: 96px; background: var(--soft-white); }
  .card-front .name { font-size: 40px; }
  .card-front .trade { font-size: 13px; }

  .contacts {
    position: absolute;
    left: 40px;
    right: 40px;
    bottom: 30px;
    display: grid;
    grid-template-columns: 1fr 1fr;
    row-gap: 12px;
    column-gap: 18px;
    font-size: 14px;
    color: var(--ink);
  }
  .contact {
    display: flex;
    align-items: center;
    gap: 8px;
    white-space: nowrap;
  }
  .contact svg { flex: none; }
  .contact-web { grid-column: 2; }
  .social-square {
    width: 11px;
    height: 11px;
    background: var(--teal-ink);
    flex: none;
  }
</style>
</head>
<body>
<main class="stage">

  <section class="card card-back" aria-label="Business card, contact side">
    <div class="texture" role="img" aria-label="Soft faceted light grey background pattern"></div>
    <div class="wordmark">
      <span class="mark-dot"></span>
      <span class="name">Marta Quinlan</span>
      <span class="trade">Photography</span>
    </div>
    <div class="contacts">
      <div class="contact contact-phone">
        <svg width="15" height="12" viewBox="0 0 15 12" aria-hidden="true">
          <path d="M1 4 Q7.5 -1 14 4 L12 6 L10 4.5 L10 3 Q7.5 2 5 3 L5 4.5 L3 6 Z" fill="var(--teal-ink)"/>
          <rect x="3" y="6" width="9" height="5.5" rx="1" fill="var(--teal-ink)"/>
        </svg>
        <span>+61 439 271 504</span>
      </div>
      <div class="contact contact-mail">
        <svg width="14" height="10" viewBox="0 0 14 10" aria-hidden="true">
          <rect x="0.5" y="0.5" width="13" height="9" fill="var(--teal-ink)"/>
          <path d="M0.5 0.5 L7 5.5 L13.5 0.5" stroke="#fff" stroke-width="1" fill="none"/>
        </svg>
        <span>m-quinlan@brivomail.net</span>
      </div>
      <div class="contact contact-web">
        <span class="social-square"></span>
        <span>/MartaQuinlanPhotography.Aust/</span>
      </div>
    </div>
  </section>

  <section class="card card-front" aria-label="Business card, logo side">
    <div class="texture" role="img" aria-label="Soft faceted teal background pattern"></div>
    <div class="wordmark">
      <span class="mark-dot"></span>
      <span class="name">Marta Quinlan</span>
      <span class="trade">Photography</span>
    </div>
  </section>

</main>
</body>
</html>
```